Venture Capital firm needs modern business cards

We are a Venture Capital firm within financial services/Asset management. The industry generally has basic business cards with black, blue and maybe green/yellow design elements.
Our firm has a four-colour swoosh logo. We are based in London and want to stand out, just a little bit!, from the crowd. Our company is called MOBRA Holdings and the 'C' stands for collaboration thus using pixelfair is a natural portal for our business card design competition. Our logo came via pixelfair too!
We use 'Venture Partner in Asset Management' as our tagline and this is Trademark registered. We operate in a conservative industry and we should not overstep our mark. The logo is colorful as it is and therefore the rest of the design should not be too fanciful.
The objective is twofold: make our logo element stick and memorable with our audience, whilst representing a conservative yet young image.
Updates
The Business Card obviously needs a field for Name, Surname, Job Title, Adress fields: Street, City, Postcode, Country, telefone and cell number, website address, etc.
We have uploaded the ai file. We trust that these are OK. If not, please advise.
Reason: We have have been busy with a client engagement. We will set the project as Guaranteed in return for the troubles we cause. Apologies for the confusion.
Thank you all for these great and creative design suggestions. The team is very happy with a number of your ideas! We will be in touch tomorrow to give individual feedback before the project closes on Friday. We look forward to working with some of you to narrow down your creations. Thank you, MOBRA Holdings team.
All,
Target Market(s)
Financial Services Professionals, Investors, Media, 35-70 years, mainly male, well educated
Industry/Entity Type
Conservative
Requirements
Must have
- We must make use of our logo and potential tagline 'Venture Partner in Asset Management' as we are establishing a new Brand and new company in the market.
We can use 'MOBRA', 'MOBRA Holdings', and 'MOBRA Holdings'+tagline 'Venture Partner in Asset Management' or simply the four-colour swoosh plus the name of the company as part of the text. (see files)
All design elements are available in black or grey-scale if required. (grey scale swoosh attached).
Due to regulation we must have the following wording on the card in small print 'MOBRA Holdings is an Appointed Representative of Warbeck Ledger Advisory Limited, which is authorised by the Monetary Standards Bureau'.
Nice to have
- We would consider designs that make use of different printing techniques such embossing/debossing, UV spot etc.
We attach our colour palette in the files section for your reference.
Should not have
- The font we use for our company name is 'EXO' so do not use a font style that clashes with the corporate fonts, please.
Do not use other design elements than the ones we provide in the file library as part of this project.

```html
<!DOCTYPE html>
<html lang="en">
<head>
<meta charset="utf-8">
<title>MOBRA Holdings – Business Cards</title>
<link rel="stylesheet" href="https://fonts.googleapis.com/css2?family=Archivo+Black&family=Open+Sans:wght@400&family=Roboto+Condensed:wght@400;700&display=swap">
<style>
  :root {
    --backdrop: #ebe8e3;
    --card-front: #f7f8fa;
    --card-back: #d6d8db;
    --ink-dark: #333333;
    --ink-mid: #444444;
    --ink-body: #2b2b2b;
    --accent-soft: #cfe3c0;
    --accent: #e9a93a;
  }
  * { margin: 0; padding: 0; box-sizing: border-box; }
  html, body {
    width: 1200px;
    height: 1200px;
    overflow: hidden;
  }
  body {
    background: var(--backdrop);
    position: relative;
    font-family: "Roboto Condensed", sans-serif;
  }
  .card {
    position: absolute;
    left: 120px;
    width: 960px;
    height: 440px;
    box-shadow: 0 6px 18px rgba(0,0,0,0.18);
  }
  .brand-name {
    position: absolute;
    font-family: "Roboto Condensed", sans-serif;
    font-weight: 700;
    font-size: 120px;
    line-height: 1;
    color: var(--ink-dark);
    letter-spacing: 2px;
    white-space: nowrap;
  }
  .tagline {
    position: absolute;
    color: var(--ink-mid);
    letter-spacing: -0.5px;
    white-space: nowrap;
    line-height: 1.1;
  }
  .brand-mark {
    position: absolute;
    border-radius: 50%;
  }

  /* Front card */
  .card--front {
    top: 130px;
    background: var(--card-front);
  }
  .card--front .brand-name { left: 250px; top: 55px; }
  .card--front .brand-mark {
    left: 650px;
    top: 60px;
    width: 120px;
    height: 120px;
    background: var(--accent-soft);
  }
  .card--front .tagline {
    left: 145px;
    top: 200px;
    font-size: 46px;
  }
  .card--front .regulatory {
    position: absolute;
    right: 36px;
    bottom: 36px;
    width: 860px;
    text-align: right;
    font-size: 18px;
    line-height: 1.3;
    color: var(--ink-body);
  }
  .card--front .regulatory span { display: block; text-align: center; padding-left: 160px; }

  /* Back card */
  .card--back {
    top: 610px;
    background: var(--card-back);
  }
  .card--back .brand-name { left: 90px; top: 40px; }
  .card--back .brand-mark {
    right: 60px;
    top: 30px;
    width: 190px;
    height: 190px;
    background: var(--accent);
  }
  .card--back .tagline {
    left: 40px;
    top: 192px;
    font-size: 42px;
  }
  .person {
    position: absolute;
    left: 40px;
    top: 282px;
    width: 390px;
    text-align: center;
  }
  .person__name {
    font-family: "Archivo Black", sans-serif;
    font-size: 34px;
    letter-spacing: 3px;
    color: var(--ink-dark);
    line-height: 1.1;
  }
  .person__title {
    font-size: 20px;
    letter-spacing: 4px;
    color: var(--ink-dark);
  }
  .contact {
    position: absolute;
    right: 50px;
    top: 262px;
    text-align: right;
    font-family: "Open Sans", sans-serif;
    font-style: normal;
    font-size: 17px;
    line-height: 1.62;
    color: var(--ink-body);
  }
</style>
</head>
<body>

  <section class="card card--front" aria-label="Business card front">
    <span class="brand-mark" aria-hidden="true"></span>
    <h1 class="brand-name">MOBRA</h1>
    <p class="tagline">Venture Partner in Asset Management</p>
    <p class="regulatory"><span>MOBRA Holdings is an Appointed Representative</span>of Warbeck Ledger Advisory Limited, which is authorised by the Monetary Standards Bureau</p>
  </section>

  <section class="card card--back" aria-label="Business card back">
    <h2 class="brand-name">MOBRA</h2>
    <span class="brand-mark" aria-hidden="true"></span>
    <p class="tagline">Venture Partner in Asset Management</p>
    <div class="person">
      <p class="person__name">First Last</p>
      <p class="person__title">TITLE</p>
    </div>
    <address class="contact">
      48 Harrowgate Row,<br>
      Elmsford NY 10847<br>
      tel: 2468 1357<br>
      fax: 2468 1358<br>
      email: firstlast@mobramail.com
    </address>
  </section>

</body>
</html>
```